Homestead Pipeworks Service (Let every tap run steady)

We are an innovative plumbing company with over 50years experience in all plumbing sectors. we cover all areas of Perth North and South and cover residential houses to warehouse and office plumbing systems.

we are fully licencesed and fully insured and all our Plumbers are police checked for your reassurance. we have plumbers who local to most areas so call out times are usally within the hour

our plumbers are located from Dawesville to Two Rocks our plumbers are very educated and all have a minimum off 10years experience on all Plumbing sytems and Hot water systems

we can cover your plumbing system for a year for one low price from $405+gst
this is the price of one visit from some plumbers

this includes unlimited call outs includes most materials and selected fittings

for this low price includes Leaks, Blockages , Hot water breakdowns, Burst pipes, and general plumbing repairs

have piece of mind that you can call us anytime any day and we will ease the stress of your plumbing emergency

Most common problem in the house is plumbing.and water can be the most destructive. Why not take the stress and worry of calling and hoping a plumber will turn up and the out of pocket expenses it will cost you.For a cost per year that can be paid weekly or monthly will cover you for unlimited call outs and most materials to cover most works undertaken.

This low price covers you for works undertaken and most materials and unlimited call outs

Prices start from $405 this is subject to a free plumbing inspection of your property

To make this even easier we allow weekly or monthly payments if set up with direct debit

OFFICE :08 9163 2058

Emergency 0436 815 372

EMAIL homesteadpipeworksservice@mailbrook.net

Target Market(s)

general public age range 25-80yrs old

Industry/Entity Type

Plumbing

Font styles to use
Sans Serif

Colors

Designer to choose colors to be used in the design.

Requirements
Must have
• emphasis on cost and set pays
• reliabie and trustworthy
• customer confidence
• value for money
Nice to have
• can be double sided

```html
<!DOCTYPE html>
<html lang="en">
<head>
<meta charset="utf-8">
<title>Homestead Pipeworks Service – Flyer</title>
<link href="https://fonts.googleapis.com/css2?family=Montserrat:wght@600;700;800&family=Open+Sans:wght@300;400;600;700&family=Roboto+Condensed:wght@700&display=swap" rel="stylesheet">
<style>
  :root{
    --navy:#1d3f80;
    --red:#d42b27;
    --white:#ffffff;
    --ink:#1d3f80;
    --stage:#6a6a6a;
  }
  *{box-sizing:border-box;margin:0;padding:0}
  html,body{width:1200px;height:1200px;overflow:hidden}
  body{background:var(--stage);position:relative;font-family:"Open Sans",sans-serif}
  .page{position:absolute;top:245px;width:549px;height:710px;background:var(--white);overflow:hidden}
  .page--front{left:48px}
  .page--back{left:604px}

  /* front */
  .intro{position:absolute;left:0;top:0;width:306px;height:425px;padding:28px 20px 0 22px}
  .brand{text-align:center}
  .brand__mark{width:54px;height:54px;border-radius:50%;background:var(--red);margin:6px auto 14px}
  .brand__name{font-family:"Montserrat",sans-serif;font-weight:800;color:var(--navy);font-size:27px;line-height:1.02;text-transform:uppercase;letter-spacing:-.3px}
  .brand__tag{font-family:"Open Sans",sans-serif;font-weight:600;color:var(--navy);font-size:10.5px;letter-spacing:1px;margin-top:6px}
  .perks{list-style:none;margin-top:12px;padding-left:14px}
  .perks li{position:relative;font-size:10.6px;line-height:1.4;color:var(--ink);font-weight:300;margin-bottom:5px;padding-left:2px}
  .perks li::before{content:"•";position:absolute;left:-14px;font-weight:700}
  .perks b{font-weight:700}

  .offer{position:absolute;left:306px;top:0;width:243px;height:425px;background:var(--navy);color:var(--white);padding:56px 18px 0 18px}
  .offer__title{font-family:"Montserrat",sans-serif;font-weight:800;font-size:60px;line-height:.93;letter-spacing:-.5px}
  .offer__from{font-family:"Montserrat",sans-serif;font-weight:600;font-size:22px;margin-top:6px}
  .price{display:flex;align-items:flex-start;font-family:"Roboto Condensed",sans-serif;font-weight:700;line-height:1}
  .price__sign{font-size:30px;margin-top:8px}
  .price__num{font-size:76px;letter-spacing:-1px}
  .price__side{display:flex;flex-direction:column;margin-left:2px}
  .price__cents{font-size:38px;margin-top:4px}
  .price__gst{font-family:"Montserrat",sans-serif;font-weight:600;font-size:17px;margin-top:4px}
  .checks{list-style:none;margin-top:12px}
  .checks li{display:flex;gap:6px;font-size:10px;line-height:1.38;font-weight:300;margin-bottom:8px}
  .checks svg{flex:0 0 12px;margin-top:1px}

  .photo{position:absolute}
  .photo--tools{left:0;top:425px;width:549px;height:158px;background:linear-gradient(120deg,#e9ecef 0%,#cfd5db 35%,#4d78b8 50%,#b77a4a 65%,#2b2b2b 85%,#9ea4ab 100%)}
  .features{position:absolute;left:0;top:583px;width:549px;height:51px;background:var(--red);color:var(--white);font-family:"Open Sans",sans-serif;font-weight:600;font-size:11.4px;text-align:center;padding-top:9px;line-height:1.55}
  .features span{white-space:nowrap;margin:0 3px}
  .contact{position:absolute;left:0;width:549px;display:flex;align-items:center;padding-left:32px;gap:16px}
  .contact--front{top:634px;height:76px;background:var(--white)}
  .contact__phone{display:flex;align-items:center;gap:8px;font-family:"Roboto Condensed",sans-serif;font-weight:700;font-size:33px;color:var(--red)}
  .contact__lines{font-family:"Open Sans",sans-serif;font-weight:600;font-size:12.2px;color:var(--red);line-height:1.4}
  .contact__lines div{display:flex;align-items:center;gap:4px}

  /* back */
  .photo--worker{left:0;top:0;width:549px;height:299px;background:linear-gradient(100deg,#3f6fae 0%,#6d93c8 40%,#e4e7ea 70%,#f3f4f5 100%)}
  .brand--back{position:absolute;right:32px;top:40px;text-align:center;width:180px}
  .brand--back .brand__mark{width:44px;height:44px;margin:0 auto 10px}
  .brand--back .brand__name{font-size:19px}
  .brand--back .brand__tag{font-size:7.4px;letter-spacing:.4px;margin-top:4px}
  .hero{position:absolute;left:0;top:299px;width:549px;height:133px;background:var(--red);color:var(--white);display:flex;justify-content:space-between;padding:14px 32px 0 34px}
  .hero__title{font-family:"Montserrat",sans-serif;font-weight:800;font-size:37px;line-height:1.03;text-transform:uppercase;width:290px}
  .hero__note{font-family:"Open Sans",sans-serif;font-weight:400;font-size:12.6px;line-height:1.28;text-align:right;text-transform:uppercase;width:190px;padding-top:6px}
  .hero__note b{font-weight:700}
  .about{position:absolute;left:33px;top:446px;width:286px;color:var(--ink);font-size:7.7px;line-height:1.45;font-weight:400;text-align:justify}
  .about p{margin-bottom:6px}
  .photo--leak{left:327px;top:445px;width:190px;height:180px;background:radial-gradient(circle at 60% 45%,#e0b8ad 0%,#a07a45 35%,#3a342c 75%,#1f1d1b 100%)}
  .contact--back{top:640px;height:70px;background:var(--navy);padding-left:32px}
  .contact--back .contact__phone{color:var(--white);font-size:32px}
  .contact--back .contact__lines{color:var(--white)}
</style>
</head>
<body>

<section class="page page--front">
  <div class="intro">
    <div class="brand">
      <div class="brand__mark"></div>
      <div class="brand__name">Homestead Pipeworks Service</div>
      <div class="brand__tag">YOUR EMERGENCY PLUMBING COMPANY</div>
    </div>
    <ul class="perks">
      <li>We can cover your plumbing system for a year for one low price from <b>$405</b>+gst</li>
      <li>This includes unlimited call outs includes most materials and selected fittings</li>
      <li>This is the price of one visit from some plumbers</li>
      <li>For this low price includes <b>Leaks, Blockages, Hot water breakdowns, Burst pipes, and general plumbing repairs</b></li>
    </ul>
  </div>

  <div class="offer">
    <div class="offer__title">LOW<br>PRICE</div>
    <div class="offer__from">FROM</div>
    <div class="price">
      <span class="price__sign">$</span><span class="price__num">405</span>
      <span class="price__side"><span class="price__cents">.00</span><span class="price__gst">+GST</span></span>
    </div>
    <ul class="checks">
      <li><svg viewBox="0 0 12 12" width="12" height="12"><circle cx="6" cy="6" r="5" fill="none" stroke="#fff" stroke-width="1.4"/><path d="M3.4 6.1l1.9 1.9 4.6-4.9" fill="none" stroke="#fff" stroke-width="1.6"/></svg>This low price covers you for works undertaken and most materials and unlimited call outs</li>
      <li><svg viewBox="0 0 12 12" width="12" height="12"><circle cx="6" cy="6" r="5" fill="none" stroke="#fff" stroke-width="1.4"/><path d="M3.4 6.1l1.9 1.9 4.6-4.9" fill="none" stroke="#fff" stroke-width="1.6"/></svg>Prices start from $405 this is subject to a free plumbing inspection of your property</li>
      <li><svg viewBox="0 0 12 12" width="12" height="12"><circle cx="6" cy="6" r="5" fill="none" stroke="#fff" stroke-width="1.4"/><path d="M3.4 6.1l1.9 1.9 4.6-4.9" fill="none" stroke="#fff" stroke-width="1.6"/></svg>To make this even easier we allow weekly or monthly payments if set up with direct debit</li>
    </ul>
  </div>

  <div class="photo photo--tools" role="img" aria-label="Photo of plumbing tools: hard hat, blue pipe, copper pipes, black fittings and a wrench on plans"></div>

  <div class="features">
    <span>✓ No call out fee</span><span>✓ Weekly or Monthly payment plans</span><span>✓ Free Plumbing health check</span><br>
    <span>✓ Fully Insured and Licensed Plumbers</span><span>✓ Trustworthy and Realible service</span>
  </div>

  <div class="contact contact--front">
    <div class="contact__phone">
      <svg viewBox="0 0 28 28" width="26" height="26"><circle cx="14" cy="14" r="12.5" fill="none" stroke="#1d3f80" stroke-width="2"/><path d="M10 7.5c1 0 2.2 2.6 2.2 3.3 0 .8-1.3 1.2-1.3 2 0 1.3 2.6 4.3 4 4.3.8 0 1.2-1.3 2-1.3.7 0 3.3 1.2 3.3 2.2 0 1.6-1.6 2.6-3 2.6-3.6 0-9.8-6.2-9.8-9.8 0-1.4 1-3.3 2.6-3.3z" fill="#1d3f80"/></svg>
      08 9163 2058
    </div>
    <div class="contact__lines">
      <div><svg viewBox="0 0 12 12" width="11" height="11"><circle cx="6" cy="6" r="5" fill="none" stroke="#1d3f80"/><path d="M4.3 3.2c.5 0 1 1.2 1 1.5s-.6.5-.6.9c0 .6 1.2 2 1.8 2 .4 0 .6-.6.9-.6s1.5.5 1.5 1c0 .7-.7 1.1-1.4 1.1-1.6 0-4.4-2.8-4.4-4.4 0-.7.5-1.5 1.2-1.5z" fill="#1d3f80"/></svg>Emergency 0436 815 372</div>
      <div><svg viewBox="0 0 12 12" width="11" height="11"><circle cx="6" cy="6" r="5" fill="none" stroke="#1d3f80"/><rect x="3.2" y="4" width="5.6" height="4" fill="none" stroke="#1d3f80" stroke-width=".8"/><path d="M3.2 4l2.8 2.2L8.8 4" fill="none" stroke="#1d3f80" stroke-width=".8"/></svg>homesteadpipeworksservice@mailbrook.net</div>
    </div>
  </div>
</section>

<section class="page page--back">
  <div class="photo photo--worker" role="img" aria-label="Photo of a plumber in a blue cap writing on a clipboard beside a hot water system"></div>
  <div class="brand brand--back">
    <div class="brand__mark"></div>
    <div class="brand__name">Homestead Pipeworks Service</div>
    <div class="brand__tag">YOUR EMERGENCY PLUMBING COMPANY</div>
  </div>

  <div class="hero">
    <h1 class="hero__title">Let every tap run steady</h1>
    <p class="hero__note">Let every tap run steady and <b>have peace of mind</b> that you can call us anytime any day and we will ease the stress of your plumbing emergency</p>
  </div>

  <div class="about">
    <p>We are an innovative plumbing company with over 50years experience in all plumbing sectors. we cover all areas of Perth North and South and cover residential houses to warehouse and office plumbing systems.</p>
    <p>We are fully licencesed and fully insured and all our Plumbers are police checked for your reassurance. we have plumbers who are local to most areas so call out times are usally within the hour</p>
    <p>Our plumbers are located from Dawesville to Two Rocks our plumbers are very educated and all have a minimum off 10years experience on all Plumbing sytems and Hot water systems</p>
    <p>Most common problem in the house is plumbing.and water can be the most destructive. Why not take the stress and worry of calling and hoping a plumber will turn up and the out of pocket expenses it will cost you.For a cost per year that can be paid weekly or monthly will cover you for unlimited call outs and most materials to cover most works undertaken.</p>
  </div>
  <div class="photo photo--leak" role="img" aria-label="Photo of a brass pipe fitting spraying water from a leak"></div>

  <div class="contact contact--back">
    <div class="contact__phone">
      <svg viewBox="0 0 28 28" width="26" height="26"><circle cx="14" cy="14" r="12.5" fill="none" stroke="#d42b27" stroke-width="2"/><path d="M10 7.5c1 0 2.2 2.6 2.2 3.3 0 .8-1.3 1.2-1.3 2 0 1.3 2.6 4.3 4 4.3.8 0 1.2-1.3 2-1.3.7 0 3.3 1.2 3.3 2.2 0 1.6-1.6 2.6-3 2.6-3.6 0-9.8-6.2-9.8-9.8 0-1.4 1-3.3 2.6-3.3z" fill="#d42b27"/></svg>
      08 9163 2058
    </div>
    <div class="contact__lines">
      <div><svg viewBox="0 0 12 12" width="11" height="11"><circle cx="6" cy="6" r="5" fill="none" stroke="#d42b27"/><path d="M4.3 3.2c.5 0 1 1.2 1 1.5s-.6.5-.6.9c0 .6 1.2 2 1.8 2 .4 0 .6-.6.9-.6s1.5.5 1.5 1c0 .7-.7 1.1-1.4 1.1-1.6 0-4.4-2.8-4.4-4.4 0-.7.5-1.5 1.2-1.5z" fill="#d42b27"/></svg>Emergency 0436 815 372</div>
      <div><svg viewBox="0 0 12 12" width="11" height="11"><circle cx="6" cy="6" r="5" fill="none" stroke="#d42b27"/><rect x="3.2" y="4" width="5.6" height="4" fill="none" stroke="#d42b27" stroke-width=".8"/><path d="M3.2 4l2.8 2.2L8.8 4" fill="none" stroke="#d42b27" stroke-width=".8"/></svg>homesteadpipeworksservice@mailbrook.net</div>
    </div>
  </div>
</section>

</body>
</html>
```